Pamphlet for introducing people to our church

I would like a church pamphlet designed, that includes the content in file "tovik-pamphlet.txt".

I am looking for a design that will incorporate the content in a professional and creative manner.

You do not have to use the content in any specific order, but I am relying on your skill and design knowledge to organize everything in an artistic and effective way.

Target Market(s)

Everyone

Industry/Entity Type

Religious

Requirements
Must have
• logo, use of content provided, use of branding (logo colors)
Nice to have
• More images where necessary
Should not have
• cross

```html
<!DOCTYPE html>
<html lang="en">
<head>
<meta charset="utf-8">
<title>TOVIK – A Light to Every Land</title>
<link href="https://fonts.googleapis.com/css2?family=Cinzel:wght@400;500;600&family=Mulish:wght@400&display=swap" rel="stylesheet">
<style>
  :root {
    --navy: #06286a;
    --orange: #f7901e;
    --white: #ffffff;
  }
  * { margin: 0; padding: 0; box-sizing: border-box; }
  html, body { width: 927px; height: 1200px; overflow: hidden; background: var(--white); }
  .pamphlet { position: relative; width: 927px; height: 1200px; background: var(--white); }
  .hero { position: absolute; left: 0; top: 0; width: 927px; height: 952px; background: var(--navy); }
  .brand-name {
    position: absolute; left: 20px; width: 927px; top: 178px; text-align: center;
    font-family: "Cinzel", serif; font-weight: 500; font-size: 200px; line-height: 1;
    color: var(--white); letter-spacing: 2px;
  }
  .tagline {
    position: absolute; left: 0; width: 988px; top: 346px; text-align: center;
    font-family: "Cinzel", serif; font-weight: 600; font-size: 44px; line-height: 1;
    color: var(--orange); letter-spacing: 1px;
  }
  .about, .ministries {
    position: absolute; font-family: "Mulish", sans-serif; font-size: 18px;
    line-height: 25.8px; color: var(--white); text-align: center;
  }
  .about { left: 22px; top: 436px; width: 420px; }
  .about p + p { margin-top: 25.8px; }
  .divider { position: absolute; left: 463px; top: 420px; width: 8px; height: 490px; background: var(--orange); }
  .ministries { left: 484px; top: 498px; width: 418px; }
  .ministry + .ministry { margin-top: 25.8px; }
  .details {
    position: absolute; left: 0; width: 927px; top: 972px; text-align: center;
    font-family: "Cinzel", serif; font-weight: 600; font-size: 21px; line-height: 26px;
    color: var(--orange);
  }
  .contact {
    position: absolute; left: 0; width: 927px; top: 1125px; text-align: center;
    font-family: "Cinzel", serif; font-weight: 600; font-size: 21px; line-height: 26px;
    color: var(--orange);
  }
</style>
</head>
<body>
<main class="pamphlet">
  <section class="hero">
    <h1 class="brand-name">TOVIK</h1>
    <p class="tagline">A Light to Every Land</p>

    <div class="about">
      <p>TOVIK is a gathering of believers whose purpose is to seek the face of God for an authentic restoration of the church as a body of born again believers around the world. As a gathering of believers, TOVIK seeks an awakening of the mind founded on the precepts and teachings of Jesus Christ.</p>
      <p>The modern church has replaced the simple and Kingdom centered principles of Jesus’s disciples with complacent and compromised teachings on earthly prosperity. We believe in humbly seeking God without motive to use God or His Word for our own gain. The end times church will experience a glorious revival, renewed love and zeal for true discipleship, faith, and godliness as Jesus intended for us.</p>
    </div>

    <div class="divider" aria-hidden="true"></div>

    <div class="ministries">
      <p class="ministry">Mustard Seeds (Children’s ministry) ::<br>Children learn to be seeds of godliness in the world.</p>
      <p class="ministry">School of Wayfarers ::<br>Learn the basics of Christian faith and about God’s purpose for your life.</p>
      <p class="ministry">School of Servants ::<br>Deepen your knowledge of God’s word and learn how to server him.</p>
    </div>
  </section>

  <footer>
    <p class="details">Sunday Service: 10:00am-12:30pm<br>Linden Community Center<br>48 Alder Street,<br>Harbor Falls, ME 04110<br>Visit us at www.tovik.org</p>
    <p class="contact">If you need prayer or counseling give us a call at<br>+1 207-555-0147 or email us at contact@cedargrove.org</p>
  </footer>
</main>
</body>
</html>
```